Non-Profit focusing on clean water needs a poster/flyer design for our annual Stroll 2 Shore

We need a poster and flyer design for our annual Stroll 2 Shore event which will be held on Saturday, March 21st (Shared River Day) at Morrow Fern Green.

HEAD:

Think Globally, Walk Locally.

SUB:

Join K7L in Santa Barbara on Shared River Day for a Stroll 2 Shore.

PHOTOS:

(one photo of past walk – crowd scene but with one face standing out – smaller photos of our team working out of country)

SUB:

Saturday, March 21st, 10am - 2pm

HEAD

Morrow Fern Green, Santa Barbara

COPY:

For more info check out our website: www.kindrowcircle.org, or contact our Director: dana@kindrowcircle.org; 805 312 4896

K7L Logo with Tag Line

NOTHING ELSE.

The final design should communicate fun for the whole family. Blue-ish shades to denote water. Be the generation that solves the world's water crisis.

Also, no need to use the attached photos if you can come up with a cool big idea graphic.

```html
<!DOCTYPE html>
<html lang="en">
<head>
<meta charset="utf-8">
<title>Think Globally Walk Locally – Stroll 2 Shore</title>
<link href="https://fonts.googleapis.com/css2?family=League+Gothic&family=PT+Sans+Narrow:wght@400;700&family=Open+Sans:wght@400;600&display=swap" rel="stylesheet">
<style>
  :root {
    --backdrop: #5d6166;
    --teal: #0c7ea2;
    --band: #3aaed3;
    --sky-top: #bfe9f6;
    --sky-mid: #e9f8fc;
    --ink: #333a40;
    --water-light: #6cc7e6;
    --water-deep: #2a9ccc;
    --brand-dark: #231f20;
    --white: #ffffff;
  }
  * { box-sizing: border-box; margin: 0; padding: 0; }
  html, body { width: 1200px; height: 1000px; overflow: hidden; }
  body { background: var(--backdrop); position: relative; font-family: "Open Sans", sans-serif; }

  .poster {
    position: absolute; left: 290px; top: 18px; width: 620px; height: 958px;
    background: var(--white); overflow: hidden;
    box-shadow: 0 2px 10px rgba(0,0,0,.35);
  }
  .photo-crowd {
    position: absolute; left: 0; top: 0; width: 620px; height: 242px;
    background: linear-gradient(180deg, #8c8f8a 0%, #a3a59f 45%, #6f8a74 100%);
  }
  .band-top { position: absolute; left: 0; top: 242px; width: 620px; height: 12px; background: var(--band); }

  .hero {
    position: absolute; left: 0; top: 254px; width: 620px; height: 393px;
    background: radial-gradient(ellipse at 50% 40%, var(--white) 0%, var(--sky-mid) 35%, var(--sky-top) 100%);
    text-align: center; color: var(--teal);
  }
  .headline {
    position: absolute; left: 0; top: 0; width: 100%; height: 310px;
    font-family: "League Gothic", sans-serif; font-weight: 400; text-transform: uppercase;
  }
  .headline span {
    position: absolute; left: 0; width: 100%; line-height: 1; white-space: nowrap;
    -webkit-text-stroke: 2px var(--teal);
  }
  .headline .think { top: 12px; font-size: 80px; transform: scaleX(1.35); }
  .headline .globally { top: 78px; font-size: 134px; transform: scaleX(1.06); }
  .headline .walk { top: 191px; font-size: 134px; transform: scaleX(1.04); }

  .invite {
    position: absolute; top: 320px; width: 100%;
    font-family: "PT Sans Narrow", sans-serif; font-size: 16px; letter-spacing: 1.3px;
    text-transform: uppercase; line-height: 1;
  }
  .date {
    position: absolute; top: 337px; width: 100%; line-height: 1.1;
    font-family: "PT Sans Narrow", sans-serif; font-weight: 700; font-size: 30px; color: var(--ink);
  }
  .venue {
    position: absolute; top: 369px; width: 100%; line-height: 1;
    font-family: "PT Sans Narrow", sans-serif; font-size: 18px; color: var(--ink);
  }

  .info-bar {
    position: absolute; left: 0; top: 647px; width: 620px; height: 21px;
    background: var(--band); color: var(--white);
    font-family: "PT Sans Narrow", sans-serif; font-size: 13.2px; line-height: 21px; text-align: center;
    white-space: nowrap;
  }
  .info-bar strong { font-weight: 700; }

  .photo-team {
    position: absolute; left: 0; top: 668px; width: 620px; height: 146px;
    background: linear-gradient(180deg, #7e9c6a 0%, #9aa48c 40%, #8d93a3 75%, #a79480 100%);
  }
  .water {
    position: absolute; left: 0; top: 814px; width: 620px; height: 144px;
    background: linear-gradient(180deg, var(--water-light) 0%, var(--water-deep) 100%);
  }
  .brand {
    position: absolute; left: 0; top: 846px; width: 620px;
    display: flex; align-items: center; justify-content: center; gap: 12px;
    font-family: "Open Sans", sans-serif; font-weight: 600; font-size: 26px;
    color: var(--brand-dark); line-height: 1;
  }
  .brand-dot { width: 26px; height: 26px; border-radius: 50%; background: var(--brand-dark); }
  .tagline {
    position: absolute; top: 909px; width: 100%; text-align: center;
    font-size: 16.5px; color: var(--brand-dark);
  }
</style>
</head>
<body>
  <main class="poster">
    <div class="photo-crowd" role="img" aria-label="Photo of a large cheering crowd of walkers in grey event shirts giving thumbs up"></div>
    <div class="band-top"></div>

    <section class="hero">
      <h1 class="headline">
        <span class="think">Think</span>
        <span class="globally">Globally</span>
        <span class="walk">Walk Locally</span>
      </h1>
      <p class="invite">Join K7L in Santa Barbara on Shared River Day for a Stroll 2 Shore</p>
      <p class="date">SATURDAY, MARCH 21st, 10am - 2pm</p>
      <p class="venue">Morrow Fern Green, Santa Barbara</p>
    </section>

    <p class="info-bar">For more info check out our website: <strong>kindrowcircle.org</strong> or contact our director at <strong>dana@kindrowcircle.org</strong> or <strong>(805) 312-4896</strong></p>

    <div class="photo-team" role="img" aria-label="Photo of the team in a line carrying a long water pipe across a field abroad"></div>
    <div class="water" role="img" aria-label="Soft blue water surface"></div>

    <div class="brand">
      <span class="brand-dot"></span>
      <span class="brand-name">Kindrow Circle</span>
    </div>
    <p class="tagline">A Movement of Young People</p>
  </main>
</body>
</html>
```